Two Wine Labels, One Red One White

We are looking to create a brand image for our wines. There are two requirements by law that we need, however beyond that, the creativity comes from the designer. Required are:
On The Red Label, Alcohol 14.1White Label Alcohol 12.5, The Size, 750ML
SO One label for the red wine with alcohol at 14.1 in a 750 ML Bottle, and one Label for white with alcohol at 12.5 in a 750 ML bottle.

Hi All:
I have some more clarity to assist in the design work.
The Brand Name of the wine is Velmaric for both the red and the white
The name should appear as Velmaric with the Brackets around phonetical as seen here
[vel-mah-reek] Both the word and the phonetical spelling should appear.
and can be seen on wordlorebin.example The Brand Name text can be black
Label should be very light grey, I am trying to capture a Stone grey or texture from stone, although, NOT Marble.
The Red Label, The word "Red" should be in red
The White Label, The word "White" should be in White, all the original remaining elements remain as originally posted.

I look forward to hearing from you for any additional questions.
Updates

Just added a logo Not really seeing what we are trying to achieve, maybe using the logo in the design may assist

Target Market(s)

Wine Aficionados

Requirements
Must have
• Details described in Project Description above, these are required by law. The Name of the Brand will be posted shortly. For the moment if you take the project, just place red on one label and white on the other.
Nice to have
• These two wines are from California (USA), so the Sierra Nevada Mountains could be an inspiration, to outline of California or coast line, a vineyard (of course), a vine...We are in silicon valley, so there is a map of silicon valley with the Bay and ocean, something from a map could work, or let your creativity flow and not use any of these concepts.
Should not have
• I do not not care for decorative fonts, however all else is open

```html
<!DOCTYPE html>
<html lang="en">
<head>
<meta charset="utf-8">
<title>Velmaric Wine Labels</title>
<link rel="stylesheet" href="https://fonts.googleapis.com/css2?family=Cinzel:wght@400;700;900&display=swap">
<style>
  :root {
    --page: #ffffff;
    --red: #c1272d;
    --red-deep: #a11c22;
    --red-line: #d8454a;
    --red-fill: #d03238;
    --stone: #c9c9c9;
    --stone-deep: #adadad;
    --stone-line: #e4e4e4;
    --ink: #111111;
    --mark: #8a8a8a;
    --paper: #ffffff;
  }
  * { margin: 0; padding: 0; box-sizing: border-box; }
  html, body { width: 1200px; height: 1011px; overflow: hidden; background: var(--page); }
  .canvas { position: relative; width: 1200px; height: 1011px; }

  .label {
    position: absolute;
    overflow: hidden;
    font-family: "Cinzel", serif;
    font-size: 10px;
  }
  .label--red { background: var(--red); }
  .label--white { background: var(--stone); }

  .label__map {
    position: absolute;
    left: 0; top: 0; bottom: 0;
    width: 68%;
  }
  .label--red .label__map { background: linear-gradient(100deg, var(--red-deep) 0%, var(--red-deep) 50%, rgba(161,28,34,0) 100%); }
  .label--white .label__map { background: linear-gradient(100deg, var(--stone-deep) 0%, var(--stone-deep) 50%, rgba(173,173,173,0) 100%); }

  .label__square {
    position: absolute;
    left: 8.2%; top: 41.5%;
    width: 3.2em; height: 3.2em;
    background: var(--mark);
  }
  .label__name {
    position: absolute;
    left: 19%; top: 40.8%;
    font-size: 4.1em;
    font-weight: 900;
    line-height: 1;
    letter-spacing: -0.01em;
    color: var(--ink);
    white-space: nowrap;
  }
  .label__phonetic {
    position: absolute;
    left: 47.6%; top: 51.4%;
    font-size: 1.2em;
    font-weight: 700;
    letter-spacing: 0.08em;
    white-space: nowrap;
  }
  .label--red .label__phonetic { color: var(--paper); }
  .label--white .label__phonetic { color: #6a6a6a; }

  .label__title {
    position: absolute;
    left: 8.8%; top: 59%;
    font-size: 4em;
    font-weight: 700;
    line-height: 0.95;
    color: transparent;
    white-space: nowrap;
  }
  .label--red .label__title { -webkit-text-stroke: 1px var(--red-line); }
  .label--red .title__colour { color: var(--red-fill); }
  .label--white .label__title { -webkit-text-stroke: 1px var(--stone-line); }
  .label--white .title__colour { color: var(--stone-line); }

  .label__legal {
    position: absolute;
    left: 8.5%; right: 8%; top: 90.4%;
    display: flex;
    justify-content: space-between;
    font-size: 1.55em;
    font-weight: 700;
    letter-spacing: 0.02em;
    white-space: nowrap;
  }
  .label--red .label__legal { color: var(--paper); }
  .label--white .label__legal { color: #f4f4f4; }
</style>
</head>
<body>
<main class="canvas">

  <section class="label label--red" style="left:38px; top:38px; width:340px; height:441px;">
    <div class="label__map" role="img" aria-label="Coastline map of the bay area in deep red"></div>
    <div class="label__square"></div>
    <div class="label__name">Velmaric</div>
    <div class="label__phonetic">[vel-mah-reek]</div>
    <div class="label__title">The<br><span class="title__colour">Red</span><br>Label</div>
    <div class="label__legal"><span>Alcohol 14.1%</span><span>750ML</span></div>
  </section>

  <section class="label label--white" style="left:38px; top:536px; width:342px; height:441px;">
    <div class="label__map" role="img" aria-label="Coastline map of the bay area in stone grey"></div>
    <div class="label__square"></div>
    <div class="label__name">Velmaric</div>
    <div class="label__phonetic">[vel-mah-reek]</div>
    <div class="label__title">The<br><span class="title__colour">White</span><br>Label</div>
    <div class="label__legal"><span>Alcohol 12.5%</span><span>750ML</span></div>
  </section>

  <section class="label label--red" style="left:512px; top:587px; width:240px; height:310px; font-size:7.06px;">
    <div class="label__map" role="img" aria-label="Coastline map of the bay area in deep red"></div>
    <div class="label__square"></div>
    <div class="label__name">Velmaric</div>
    <div class="label__phonetic">[vel-mah-reek]</div>
    <div class="label__title">The<br><span class="title__colour">Red</span><br>Label</div>
    <div class="label__legal"><span>Alcohol 14.1%</span><span>750ML</span></div>
  </section>

  <section class="label label--white" style="left:865px; top:405px; width:220px; height:311px; font-size:6.6px;">
    <div class="label__map" role="img" aria-label="Coastline map of the bay area in stone grey"></div>
    <div class="label__square"></div>
    <div class="label__name">Velmaric</div>
    <div class="label__phonetic">[vel-mah-reek]</div>
    <div class="label__title">The<br><span class="title__colour">White</span><br>Label</div>
    <div class="label__legal"><span>Alcohol 12.5%</span><span>750ML</span></div>
  </section>

</main>
</body>
</html>
```